Postcard Design Project

Home improvement specializing in KORV Roofing Windows, Siding and Guttersif you have worked with such companines before,,grab some idea..Coupons on the back could say something like free gutters with Roof purchaseFree Gutters with SidingCheck out our website prestigehomesolutions.netI am an individual sales person looking for advantage over the rest.

Industry/Entity Type

Home Improvement

```html
<!DOCTYPE html>
<html lang="en">
<head>
<meta charset="utf-8">
<title>Brightwell Home Works Postcard</title>
<link rel="stylesheet" href="https://fonts.googleapis.com/css2?family=Oswald:wght@400;500;600;700&family=Roboto:wght@400;700&display=swap">
<style>
:root{
  --olive:#b4b42a;
  --olive-dark:#9d9d1f;
  --ink:#2b2b2b;
  --footer:#2a2a2a;
  --red:#e2202a;
  --silver-light:#f4f4f4;
  --silver-dark:#bdbdbd;
  --white:#ffffff;
  --stage:#e3e3e3;
}
*{box-sizing:border-box;margin:0;padding:0}
html,body{width:1200px;height:1066px;overflow:hidden}
body{background:var(--stage);position:relative;font-family:"Oswald",sans-serif}
.card{position:absolute;top:82px;width:492px;height:904px;overflow:hidden;background:var(--olive);box-shadow:0 6px 18px rgba(0,0,0,.25)}
.card--front{left:89px}
.card--back{left:618px}
.card-art{position:absolute;left:0;top:0}
.brand{position:absolute;left:0;right:0;top:40px;display:flex;align-items:center;justify-content:center;gap:16px}
.brand-dot{width:62px;height:62px;border-radius:50%;background:var(--olive)}
.brand-name{font-family:"Oswald",sans-serif;font-weight:500;color:var(--ink);line-height:1.05;font-size:34px;letter-spacing:1px;text-transform:uppercase}
.brand-name span{display:block}
.tagline{position:absolute;left:0;right:0;text-align:center;text-transform:uppercase;font-family:"Oswald",sans-serif}
.tagline--lead{top:664px;font-size:24px;font-weight:600;color:var(--ink)}
.tagline--big{top:700px;font-size:62px;font-weight:600;color:var(--white);letter-spacing:.5px;line-height:1.1}
.tagline--tail{top:770px;font-size:27px;font-weight:600;color:var(--ink)}
.footer{position:absolute;left:0;right:0;bottom:0;height:72px;background:var(--footer);color:var(--white)}
.call{position:absolute;left:26px;top:9px}
.call-label{font-family:"Oswald",sans-serif;font-weight:600;font-size:17px;line-height:1.1}
.call-number{font-family:"Oswald",sans-serif;font-weight:600;font-size:29px;line-height:1.1}
.footer-rule{position:absolute;left:232px;top:12px;width:1px;height:48px;background:#6a6a6a}
.contact{position:absolute;left:253px;font-family:"Roboto",sans-serif;font-weight:700;font-size:12.5px;display:flex;align-items:center;gap:9px}
.contact--web{top:14px}
.contact--mail{top:41px}
.contact-dot{width:17px;height:17px;border-radius:50%;background:#8a8a8a;display:flex;align-items:center;justify-content:center}
.coupon{position:absolute;left:23px;top:257px;width:448px;height:295px;border:2px dashed #8c8c8c;border-radius:12px;background:linear-gradient(180deg,#f1f1f1,#c9c9c9);text-align:center}
.coupon .brand{top:22px;gap:12px}
.coupon .brand-dot{width:44px;height:44px}
.coupon .brand-name{font-size:24px}
.coupon-free{position:absolute;left:0;right:0;top:92px;font-family:"Oswald",sans-serif;font-weight:700;font-size:82px;line-height:1;color:var(--red)}
.coupon-main{position:absolute;left:0;right:0;top:192px;font-family:"Oswald",sans-serif;font-weight:600;font-size:25px;color:var(--ink)}
.coupon-sub{position:absolute;left:0;right:0;top:230px;font-family:"Oswald",sans-serif;font-weight:500;font-size:17px;color:var(--ink)}
.scissors{position:absolute;left:42px;top:240px}
.services-btn{position:absolute;left:137px;top:590px;width:213px;height:47px;border-radius:8px;background:var(--ink);color:var(--white);font-family:"Roboto",sans-serif;font-size:19px;display:flex;align-items:center;justify-content:center;letter-spacing:.3px}
.service{position:absolute;top:692px;width:120px;text-align:center}
.service-label{display:block;margin-top:6px;font-family:"Roboto",sans-serif;font-size:18px;color:var(--ink)}
.service--roof{left:47px}
.service--windows{left:185px}
.service--siding{left:322px}
.service-rule{position:absolute;top:669px;width:1px;height:109px;background:#6f6f18}
.service-rule--a{left:176px}
.service-rule--b{left:311px}
</style>
</head>
<body>

<section class="card card--front">
  <svg class="card-art" width="492" height="632" viewBox="0 0 492 632">
    <defs>
      <linearGradient id="silverA" x1="0" y1="0" x2="0" y2="1">
        <stop offset="0" stop-color="#f4f4f4"/><stop offset="1" stop-color="#bcbcbc"/>
      </linearGradient>
      <linearGradient id="houseTone" x1="0" y1="0" x2="0" y2="1">
        <stop offset="0" stop-color="#93b7d8"/>
        <stop offset=".4" stop-color="#8a4a36"/>
        <stop offset=".75" stop-color="#d6a25a"/>
        <stop offset="1" stop-color="#b0763e"/>
      </linearGradient>
    </defs>
    <rect width="492" height="270" fill="url(#silverA)"/>
    <polygon points="0,218 246,150 492,218 492,238 246,170 0,238" fill="#ffffff"/>
    <polygon points="0,238 246,170 492,238 492,258 246,190 0,258" fill="var(--olive)"/>
    <g role="img" aria-label="Photo of a brick house with a brown tiled roof under a blue sky">
      <polygon points="0,258 246,190 492,258 492,632 0,632" fill="url(#houseTone)"/>
    </g>
  </svg>
  <div class="brand">
    <div class="brand-dot"></div>
    <div class="brand-name"><span>Brightwell</span><span>Home Works</span></div>
  </div>
  <p class="tagline tagline--lead">If you have worked with such</p>
  <p class="tagline tagline--big">Companines</p>
  <p class="tagline tagline--tail">Before,grab some idea..</p>
  <footer class="footer">
    <div class="call"><div class="call-label">CALL NOW</div><div class="call-number">877-555-0142</div></div>
    <div class="footer-rule"></div>
    <div class="contact contact--web"><span class="contact-dot"></span>www.brightwellhouseworks.net</div>
    <div class="contact contact--mail"><span class="contact-dot"></span>info@brightwellhouseworks.net</div>
  </footer>
</section>

<section class="card card--back">
  <svg class="card-art" width="492" height="270" viewBox="0 0 492 270">
    <defs>
      <linearGradient id="silverB" x1="0" y1="0" x2="0" y2="1">
        <stop offset="0" stop-color="#f4f4f4"/><stop offset="1" stop-color="#bcbcbc"/>
      </linearGradient>
    </defs>
    <rect width="492" height="270" fill="url(#silverB)"/>
    <polygon points="0,228 246,160 492,228 492,248 246,180 0,248" fill="#ffffff"/>
    <polygon points="0,248 246,180 492,248 492,270 0,270" fill="var(--olive)"/>
  </svg>
  <div class="brand">
    <div class="brand-dot"></div>
    <div class="brand-name"><span>Brightwell</span><span>Home Works</span></div>
  </div>
  <div class="coupon">
    <div class="brand">
      <div class="brand-dot"></div>
      <div class="brand-name"><span>Brightwell</span><span>Home Works</span></div>
    </div>
    <p class="coupon-free">FREE</p>
    <p class="coupon-main">GUTTERS WITH ROOF PURCHASE</p>
    <p class="coupon-sub">FREE GUTTERS WITH SIDING</p>
  </div>
  <svg class="scissors" width="22" height="22" viewBox="0 0 22 22" fill="none" stroke="#333" stroke-width="1.6">
    <circle cx="5" cy="17" r="3"/><circle cx="11" cy="19" r="3"/>
    <line x1="7" y1="15" x2="19" y2="3"/><line x1="10" y1="16" x2="6" y2="3"/>
  </svg>
  <div class="services-btn">OUR SERVICES</div>
  <div class="service-rule service-rule--a"></div>
  <div class="service-rule service-rule--b"></div>
  <div class="service service--roof">
    <svg width="54" height="58" viewBox="0 0 54 58">
      <polygon points="27,2 51,15 51,43 27,56 3,43 3,15" fill="#fff" stroke="#333" stroke-width="2"/>
      <polygon points="27,17 40,29 36,29 36,40 18,40 18,29 14,29" fill="#222"/>
      <rect x="24" y="32" width="6" height="8" fill="#fff"/>
    </svg>
    <span class="service-label">Roofing</span>
  </div>
  <div class="service service--windows">
    <svg width="54" height="58" viewBox="0 0 54 58">
      <polygon points="27,2 51,15 51,43 27,56 3,43 3,15" fill="#fff" stroke="#333" stroke-width="2"/>
      <rect x="17" y="19" width="20" height="20" fill="none" stroke="#222" stroke-width="2.5"/>
      <line x1="27" y1="19" x2="27" y2="39" stroke="#222" stroke-width="2"/>
      <line x1="17" y1="29" x2="37" y2="29" stroke="#222" stroke-width="2"/>
    </svg>
    <span class="service-label">Windows</span>
  </div>
  <div class="service service--siding">
    <svg width="54" height="58" viewBox="0 0 54 58">
      <polygon points="27,2 51,15 51,43 27,56 3,43 3,15" fill="#fff" stroke="#333" stroke-width="2"/>
      <rect x="18" y="18" width="18" height="5" fill="#222"/>
      <rect x="18" y="25" width="18" height="5" fill="#222"/>
      <rect x="18" y="32" width="18" height="5" fill="#222"/>
    </svg>
    <span class="service-label">Siding</span>
  </div>
  <footer class="footer">
    <div class="call"><div class="call-label">CALL NOW</div><div class="call-number">877-555-0142</div></div>
    <div class="footer-rule"></div>
    <div class="contact contact--web"><span class="contact-dot"></span>www.brightwellhouseworks.net</div>
    <div class="contact contact--mail"><span class="contact-dot"></span>info@brightwellhouseworks.net</div>
  </footer>
</section>

</body>
</html>
```